Holloway Photography.
I really don't know what should go here
Simple
Glen Holloway
Owner
4820 NE Corvel Dr Ankeny Ia 50023
holloway.photography@brevanmail.com
hollowayphotography.net
I am thinking that i will put a photo, or just my logo on one side, and the rest of the info on the other.
This is one of those moments...
let us tell your story.

```html
<!DOCTYPE html>
<html lang="en">
<head>
<meta charset="utf-8">
<title>Holloway Photography — Stationery Set</title>
<link href="https://fonts.googleapis.com/css2?family=Cinzel:wght@400;600&family=Lato:wght@400;700&display=swap" rel="stylesheet">
<style>
  :root{
    --bg:#e4e1dc;
    --paper:#ffffff;
    --grey-card:#dcdcdc;
    --ink:#2a2a2a;
    --ink-soft:#6b6b6b;
    --rule:#c9c9c9;
    --night:#1c1c1c;
    --night-mid:#3a3a3a;
    --swirl:#ececec;
  }
  *{margin:0;padding:0;box-sizing:border-box}
  html,body{width:1200px;height:665px;overflow:hidden;background:var(--bg)}
  body{position:relative;font-family:'Lato',sans-serif;color:var(--ink)}
  .piece{position:absolute;background:var(--paper);box-shadow:0 3px 8px rgba(0,0,0,.25)}
  .brand{font-family:'Cinzel',serif;font-weight:600;color:var(--ink);letter-spacing:.06em;line-height:1.1;display:flex;align-items:center;gap:5px}
  .brand::before{content:"";width:8px;height:8px;border-radius:50%;background:currentColor;flex:none}
  .brand.light{color:#f2f2f2}
  .brand.center{justify-content:center}
  .tiny{font-size:6px;line-height:1.5;color:var(--ink-soft)}
  .name{font-family:'Cinzel',serif;font-size:9px;font-weight:600;color:var(--ink)}
  .role{font-size:6px;color:var(--ink-soft);margin-bottom:6px}
  .night-photo{position:absolute;inset:0;background:radial-gradient(ellipse at 60% 35%,#6d6d6d 0%,var(--night-mid) 35%,var(--night) 80%)}
  .swirl{position:absolute;background:linear-gradient(160deg,transparent 10%,var(--swirl) 55%,transparent 95%)}

  /* business cards, landscape */
  .card-front{left:230px;top:80px;width:160px;height:146px;padding:14px}
  .card-front .brand{font-size:8px;margin:0 0 14px 40px}
  .card-back{left:396px;top:78px;width:128px;height:148px;background:var(--night);overflow:hidden}
  .card-back .brand{position:absolute;left:10px;right:10px;top:62px;font-size:8px}

  /* vertical cards */
  .card-grey{left:86px;top:240px;width:160px;height:192px;background:var(--grey-card);padding:14px}
  .card-grey .photo-slot{position:absolute;left:14px;top:16px;width:34px;height:40px;background:linear-gradient(#bdbdbd,#9d9d9d)}
  .card-grey .who{position:absolute;left:14px;top:72px}
  .card-grey .tiny{position:absolute;left:14px;bottom:16px}
  .card-grey .tiny.right{left:auto;right:14px;text-align:right;top:100px;bottom:auto}
  .card-white-v{left:264px;top:233px;width:120px;height:199px;padding:14px 10px;text-align:center}
  .card-white-v .brand{font-size:7px;margin-bottom:20px}
  .card-white-v .tiny{margin-top:20px}
  .card-dark-v{left:400px;top:233px;width:121px;height:199px;background:var(--night);overflow:hidden}
  .card-dark-v .brand{position:absolute;left:8px;right:8px;bottom:30px;font-size:7px}
  .card-dark-v .tiny{position:absolute;left:0;right:0;bottom:12px;text-align:center;color:#aaa;font-size:5px}

  /* letterhead */
  .letterhead{left:533px;top:82px;width:295px;height:458px;overflow:hidden}
  .letterhead .brand{position:absolute;left:28px;top:24px;width:100px;font-size:8px}
  .letterhead .contact{position:absolute;left:170px;top:26px}
  .letterhead .swirl{left:0;right:0;bottom:0;height:150px}

  /* fax */
  .fax{left:845px;top:82px;width:307px;height:458px;overflow:hidden}
  .fax .brand{position:absolute;left:26px;top:24px;width:100px;font-size:8px}
  .fax .contact{position:absolute;left:176px;top:26px}
  .fax-title{position:absolute;right:26px;top:70px;font-family:'Cinzel',serif;font-weight:600;font-size:12px}
  .fax-fields{position:absolute;left:26px;right:26px;top:92px;display:grid;grid-template-columns:1fr 1fr;gap:6px 16px}
  .field{font-size:6px;color:var(--ink-soft);border-bottom:1px solid var(--rule);padding-bottom:2px}
  .fax-checks{position:absolute;left:26px;right:26px;top:148px;display:flex;justify-content:space-between;font-size:5.5px;color:var(--ink-soft)}
  .fax-checks span::before{content:"";display:inline-block;width:5px;height:5px;border:1px solid var(--rule);margin-right:3px;vertical-align:-1px}
  .fax-rule{position:absolute;left:26px;right:26px;top:162px;border-top:1px solid var(--rule)}
  .fax .swirl{left:0;right:0;bottom:0;height:150px}

  /* envelope */
  .envelope{left:86px;top:475px;width:298px;height:139px;padding:14px}
  .envelope .brand{font-size:8px}
  .envelope .tiny{position:absolute;left:14px;bottom:14px}

  .flaps{position:absolute;left:396px;top:475px}
</style>
</head>
<body>

<div class="piece card-front">
  <p class="brand">Holloway Photography</p>
  <p class="name">Glen Holloway</p>
  <p class="role">Owner</p>
  <p class="tiny">4820 NE Corvel Dr<br>Ankeny Ia 50023<br><br>Phone: 515-555-0148<br>holloway.photography@brevanmail.com</p>
</div>

<div class="piece card-back">
  <div class="night-photo" role="img" aria-label="Dark night-sky photograph with soft sparkles"></div>
  <p class="brand light center">Holloway Photography</p>
</div>

<div class="piece card-grey">
  <div class="photo-slot" role="img" aria-label="Small portrait photo placeholder"></div>
  <div class="who"><p class="name">Glen Holloway</p><p class="role">Owner</p></div>
  <p class="tiny right">Phone: 515-555-0148<br>Fax: 515-555-0149</p>
  <p class="tiny">holloway.photography@brevanmail.com<br>hollowayphotography.net</p>
</div>

<div class="piece card-white-v">
  <p class="brand center">Holloway Photography</p>
  <p class="name">Glen Holloway</p>
  <p class="role">Owner</p>
  <p class="tiny">4820 NE Corvel Dr<br>Ankeny Ia 50023</p>
  <p class="tiny">515-555-0148<br>hollowayphotography.net</p>
</div>

<div class="piece card-dark-v">
  <div class="night-photo" role="img" aria-label="Dark night-sky photograph with soft sparkles"></div>
  <p class="brand light center">Holloway Photography</p>
  <p class="tiny">let us tell your story.</p>
</div>

<div class="piece letterhead">
  <p class="brand">Holloway Photography</p>
  <p class="tiny contact">4820 NE Corvel Dr<br>Ankeny Ia 50023<br>Phone: 515-555-0148<br>holloway.photography@brevanmail.com</p>
  <div class="swirl" role="img" aria-label="Faint grey flourish decoration"></div>
</div>

<div class="piece fax">
  <p class="brand">Holloway Photography</p>
  <p class="tiny contact">4820 NE Corvel Dr<br>Ankeny Ia 50023<br>Phone: 515-555-0148<br>holloway.photography@brevanmail.com</p>
  <p class="fax-title">FAX</p>
  <div class="fax-fields">
    <p class="field">To:</p><p class="field">From:</p>
    <p class="field">Fax:</p><p class="field">Pages:</p>
    <p class="field">Phone:</p><p class="field">Date:</p>
    <p class="field">Re:</p><p class="field">CC:</p>
  </div>
  <div class="fax-checks">
    <span>Urgent</span><span>For Review</span><span>Please Comment</span><span>Please Reply</span><span>Recycle</span>
  </div>
  <div class="fax-rule"></div>
  <div class="swirl" role="img" aria-label="Faint grey flourish decoration"></div>
</div>

<div class="piece envelope">
  <p class="brand">Holloway Photography</p>
  <p class="tiny">4820 NE Corvel Dr<br>Ankeny Ia 50023<br>hollowayphotography.net</p>
</div>

<svg class="flaps" width="764" height="140" viewBox="0 0 764 140" aria-hidden="true">
  <defs>
    <filter id="lift" x="-5%" y="-10%" width="110%" height="130%"><feDropShadow dx="0" dy="2" stdDeviation="2.5" flood-opacity=".25"/></filter>
  </defs>
  <g filter="url(#lift)">
    <rect x="0" y="0" width="228" height="139" fill="#ffffff"/>
    <polygon points="0,0 228,0 228,18 114,58 0,18" fill="#f1f1f1" stroke="#d4d4d4"/>
    <rect x="228" y="0" width="216" height="139" fill="#e9e9e9"/>
    <polygon points="228,0 444,0 444,18 336,58 228,18" fill="#bdbdbd"/>
    <rect x="444" y="0" width="320" height="139" fill="#ffffff"/>
    <polygon points="444,0 764,0 764,18 604,70 444,18" fill="#1c1c1c"/>
  </g>
  <text x="114" y="32" text-anchor="middle" font-family="Cinzel, serif" font-weight="600" font-size="7" fill="#2a2a2a" letter-spacing=".4">Holloway Photography</text>
  <text x="336" y="32" text-anchor="middle" font-family="Cinzel, serif" font-weight="600" font-size="7" fill="#2a2a2a" letter-spacing=".4">Holloway Photography</text>
  <text x="604" y="34" text-anchor="middle" font-family="Cinzel, serif" font-weight="600" font-size="8" fill="#f2f2f2" letter-spacing=".4">Holloway Photography</text>
</svg>

</body>
</html>
```